Modern Website Design for an Online Travel Agency.. Design Only!!

Hi there!

We are building an website for our travel agency that caters to tourists traveling to the Cayman Islands. We provide travel information and take bookings for various tours available here.

We need designs for 8 different web page layouts. You can see the layout specifications in two attached documents. We do not have a need for the coding to be done. This will simply act as a blueprint for our developer to build from.

The important pages are the 'Home Page' 'checkout page' and the ‘Checkout Page’ (Page 1 & 10 in the PDF ‘Website Layout’)

The MOST important page is ‘Tour Search Page’ (page 6)

If you intend on only submitting one page design, please submit a design for page 6. Be aware though, the more of these 3 page designs you submit, the more likely we are to move forward with you!

At this stage, we are simply looking to develop the most aesthetic website design layout possible.

- The website should be colour coordinated with the logo. You can most certainly use other colours if you feel they complement the overall design of the website well.

- Everything must be laid out in an EXTREMELY simple & ‘easy to navigate’ way. The key is simplicity & Functionality. There is no need for messy or elaborate graphics.

- The website MUST have a VERY clean and modern appearance.

- We want the main background to be white, but you can use light grey in places to compliment or add dimension if you feel necessary.

- We will appreciate a good use of shadows and especially a good use of icons. (You can see examples of icons we have already designed, we are definitely open to new icon design concepts too)

- We will reward imagination and original thinking! Essentially we want a website with a creative touch and unique design elements, whilst maintaining that clean and simple layout.

- Most importantly!! - Paying attention to the small details will be highly rewarded (A well balanced and seamless use of fonts, colours, dimensions, shadowing, positioning, etc)

If you have any questions, please don’t hesitate to ask.

We’re excited to see your design submissions!

Thank you!!

You can find all the support documents and content at: https://www.filevorra.net/sh/9qm2rtwplexan7c/QQBmTtZnPdLsWEGxvvaJpLmRw?dl=0

Target Market(s)

Tourists

Industry/Entity Type

Travel

Number of Pages Required

5+ page

Font styles to use
Sans Serif

Colors

Designer to choose colors to be used in the design.

Requirements
Must have
• Must be very clean and modern.
• Must be simple and bold
• Must be color coordinated in a way that makes sense
• White background
Nice to have
• Good use of shadows and Icons
Should not have
• Over use of messy graphics
• And design layout which is not right angled (using anything but vertical or horizontal for the edges in the design)

```html
<!DOCTYPE html>
<html lang="en">
<head>
<meta charset="utf-8">
<title>Tidewell Travel – Home</title>
<link rel="stylesheet" href="https://fonts.googleapis.com/css2?family=Montserrat:wght@500;600;700;800;900&family=Lato:wght@400;700&display=swap">
<style>
  :root {
    --header-blue: #1c72d4;
    --brand-blue: #1a6bd8;
    --accent-green: #9cc93c;
    --cta-yellow: #f4d83a;
    --cta-blue: #2196f3;
    --text-dark: #1e1e1e;
    --panel-grey: #ebebeb;
    --white: #ffffff;
  }
  * { margin: 0; padding: 0; box-sizing: border-box; }
  html, body { width: 1200px; height: 1147px; overflow: hidden; background: var(--white); }
  body { position: relative; font-family: "Lato", sans-serif; color: var(--text-dark); }

  .site-header {
    position: absolute; left: 0; top: 0; width: 1200px; height: 90px;
    background: var(--header-blue);
    box-shadow: 0 2px 6px rgba(0,0,0,.18);
    z-index: 2;
  }
  .brand {
    position: absolute; left: 72px; top: 30px;
    display: flex; align-items: center; gap: 8px;
    font-family: "Montserrat", sans-serif; font-weight: 700; font-size: 24px;
    color: var(--accent-green);
  }
  .brand-mark { width: 30px; height: 30px; background: var(--accent-green); border-radius: 4px; }

  .social-links { position: absolute; left: 766px; top: 30px; display: flex; gap: 8px; }
  .social-links span { width: 18px; height: 18px; border-radius: 3px; background: rgba(255,255,255,.55); }

  .utility-bar {
    position: absolute; left: 978px; top: 29px; display: flex; gap: 26px;
    font-family: "Montserrat", sans-serif; font-weight: 600; font-size: 11px; color: var(--white);
  }
  .utility-bar .currency b { color: var(--accent-green); font-size: 13px; margin-left: 2px; }
  .utility-bar .login { display: flex; align-items: center; gap: 8px; }

  .main-nav {
    position: absolute; left: 552px; top: 62px; display: flex; gap: 20px;
    font-family: "Montserrat", sans-serif; font-weight: 600; font-size: 12.3px;
    letter-spacing: .05em; color: var(--white);
  }
  .main-nav a { color: inherit; text-decoration: none; position: relative; }
  .main-nav a.is-active::after {
    content: ""; position: absolute; left: 38px; right: 40px; top: 26px; height: 2px;
    background: var(--accent-green);
  }

  .hero { position: absolute; left: 0; top: 90px; width: 1200px; height: 538px; }
  .hero-photo {
    position: absolute; inset: 0;
    background: linear-gradient(180deg, #5f8dc4 0%, #9bb8d8 38%, #6d9ac0 50%, #2f7ea8 56%, #1e86a3 75%, #1e97a8 100%);
  }
  .hero-copy { position: absolute; left: 60px; width: 622px; top: 0; text-align: center; color: var(--white); }
  .hero-title {
    margin-top: 150px;
    font-family: "Montserrat", sans-serif; font-weight: 900; font-size: 53px; letter-spacing: -.01em;
    text-shadow: 0 3px 6px rgba(0,0,0,.35);
  }
  .hero-subtitle {
    margin-top: 8px;
    font-family: "Montserrat", sans-serif; font-weight: 900; font-size: 28px; letter-spacing: .5em;
    text-shadow: 0 3px 6px rgba(0,0,0,.35);
  }
  .hero-text {
    margin-top: 24px; font-size: 13.5px; line-height: 20px; font-weight: 700;
    text-shadow: 0 1px 3px rgba(0,0,0,.5);
  }
  .btn {
    position: absolute; display: flex; align-items: center; justify-content: center;
    font-family: "Montserrat", sans-serif; font-weight: 600; border-radius: 3px;
  }
  .btn-hero {
    left: 290px; top: 364px; width: 163px; height: 43px;
    background: var(--cta-yellow); color: var(--text-dark); font-size: 11px;
    box-shadow: 0 3px 6px rgba(0,0,0,.25);
  }

  .welcome { position: absolute; left: 0; top: 628px; width: 1200px; height: 465px; background: var(--panel-grey); }
  .welcome-photo {
    position: absolute; left: 38px; top: 64px; width: 514px; height: 342px;
    background: linear-gradient(180deg, #7fd3d6 0%, #2fb3c2 45%, #178fa6 70%, #6a7a4e 100%);
  }
  .welcome-title {
    position: absolute; left: 647px; top: 44px;
    font-family: "Montserrat", sans-serif; font-weight: 800; font-size: 29px; color: var(--brand-blue);
  }
  .welcome-text {
    position: absolute; left: 650px; top: 100px; width: 418px;
    font-size: 13.4px; line-height: 36.1px;
  }
  .btn-welcome {
    left: 655px; top: 387px; width: 112px; height: 29px;
    background: var(--cta-blue); color: var(--white); font-size: 8.5px; font-weight: 500;
  }

  .world-strip {
    position: absolute; left: 0; top: 1093px; width: 1200px; height: 54px;
    background: linear-gradient(180deg, #ffffff 0%, #f1f4f8 100%);
  }
</style>
</head>
<body>
  <header class="site-header">
    <div class="brand"><span class="brand-mark"></span>Tidewell</div>
    <div class="social-links" aria-label="Social links"><span></span><span></span><span></span><span></span></div>
    <div class="utility-bar">
      <span class="currency">USD<b>$</b></span>
      <span class="login">Login
        <svg width="15" height="15" viewBox="0 0 16 16" fill="none" stroke="#9cc93c" stroke-width="1.4">
          <rect x="2" y="7" width="12" height="8" rx="1.5"/><path d="M5 7V4.5a3 3 0 0 1 6 0V7"/>
        </svg>
      </span>
    </div>
    <nav class="main-nav">
      <a class="is-active" href="#">DISCOVER CAYMAN</a>
      <a href="#">THING TO DO</a>
      <a href="#">MY TRIP PLANNER</a>
      <a href="#">MAP</a>
      <a href="#">CONTACT US</a>
    </nav>
  </header>

  <section class="hero">
    <div class="hero-photo" role="img" aria-label="Photo of a boy jumping over the sea under a cloudy sky"></div>
    <div class="hero-copy">
      <h1 class="hero-title">Start Your Greatest</h1>
      <p class="hero-subtitle">ADVENTURE WITH US!</p>
      <p class="hero-text">Lorem ipsum dolor sit amet, consectetur adipiscing elit, sed do eiusmod tempor incididunt<br>ut labore et dolore magna aliqua. Ut enim ad minim veniam.</p>
    </div>
    <a class="btn btn-hero" href="#">CLICK HERE</a>
  </section>

  <section class="welcome">
    <div class="welcome-photo" role="img" aria-label="Underwater photo of snorkelers above a coral reef"></div>
    <h2 class="welcome-title">Welcome to Tidewell Travel</h2>
    <p class="welcome-text">We are proud travel concierges of the Cayman Islands! We help thousands of tourists visiting Cayman every year arrange vacation getaway catered to their exact needs. With a wealth of local knowledge, we help you avoid unreliable tour operators and find those local hidden gems. Here you can research everything you need to be fully prepared for your travels and also view the complete range of activities available</p>
    <a class="btn btn-welcome" href="#">CLICK HERE</a>
  </section>

  <div class="world-strip" role="img" aria-label="Faint dotted world map with travel illustrations"></div>
</body>
</html>
```